Business Card Design for Kidvale (Hires out childrens play areas)

Looking to have a business card designed for a company we just bought. The company rents out childrens play areas.

I have uploaded a couple of examples of the kind of business card style I like. Here are two more examples:

https://quorvastudio.nz/project/bright-romp-branding/
https://imgvaultcdn.com/design_img/8841052/302917/302917_5518203_8841052_b73e19a2_image.jpg

I think a white card will be best due to all the colours in the logo.

Size we require: 3.75" x 2.25" (horizontally orientated) with a 0.125" bleed

Uploaded is two versions of our logo.

Details for the card:
1. My name: Liam Verster
2. Title: Managing Director
3. Phone no: 021 563 417
4. Email: liam@kidvale.co.nz
5. URL: www.kidvale.co.nz
6. Address:
PO Box 318625
Fernlea, Auckland

Let me know if you need anything else.

Target Market(s)

Hospitals, doctors surgeries, bed shops, etc.

Contact Information for Business Card

Details for the card:
1. My name: Liam Verster
3. Phone no: 021 563 417
5. URL: www.kidvale.co.nz
6. Address:
PO Box 318625
Fernlea, Auckland

Requirements
Should not have
• Not too busy.

```html
<!DOCTYPE html>
<html lang="en">
<head>
<meta charset="utf-8">
<title>Kidvale Business Card</title>
<link href="https://fonts.googleapis.com/css2?family=Montserrat:wght@700&family=Questrial&display=swap" rel="stylesheet">
<style>
  :root {
    --page-bg: #e9e9e9;
    --card-bg: #ffffff;
    --card-edge: #d2d2d2;
    --brand-blue: #1a5ca8;
    --ink: #333438;
    --ink-soft: #4a4b50;
    --pattern-red: #f4cfd0;
    --pattern-blue: #cfdcf1;
    --pattern-orange: #fbe3c2;
    --pattern-purple: #e4d3ea;
  }
  * { margin: 0; padding: 0; box-sizing: border-box; }
  html, body {
    width: 1200px;
    height: 1200px;
    overflow: hidden;
    background: var(--page-bg);
  }
  .sheet {
    position: relative;
    width: 1200px;
    height: 1200px;
  }
  .card {
    position: absolute;
    left: 237px;
    width: 727px;
    height: 436px;
    background: var(--card-bg);
    border: 1px solid var(--card-edge);
    overflow: hidden;
  }
  .card--front { top: 100px; }
  .card--back { top: 600px; }

  .identity {
    position: absolute;
    left: 60px;
    width: 280px;
    top: 140px;
    text-align: center;
  }
  .wordmark {
    display: inline-flex;
    align-items: center;
    gap: 8px;
    font-family: "Questrial", sans-serif;
    font-size: 34px;
    color: var(--brand-blue);
    letter-spacing: 0.5px;
  }
  .wordmark__dot {
    width: 14px;
    height: 14px;
    border-radius: 50%;
    background: var(--brand-blue);
  }
  .person__name {
    margin-top: 38px;
    font-family: "Montserrat", sans-serif;
    font-weight: 700;
    font-size: 31px;
    color: var(--brand-blue);
    line-height: 1;
  }
  .person__title {
    margin-top: 10px;
    font-family: "Questrial", sans-serif;
    font-size: 19px;
    color: var(--ink-soft);
  }

  .contact {
    position: absolute;
    right: 37px;
    top: 120px;
    text-align: right;
    font-family: "Questrial", sans-serif;
    font-size: 25px;
    color: var(--ink);
    line-height: 33px;
  }
  .contact__line {
    display: flex;
    justify-content: flex-end;
    align-items: center;
    gap: 7px;
  }
  .contact__icon {
    width: 14px;
    height: 14px;
    flex: none;
  }
  .contact__address { margin-top: 18px; }

  .pattern {
    width: 100%;
    height: 100%;
    background:
      radial-gradient(circle at 18% 30%, var(--pattern-blue) 0, transparent 28%),
      radial-gradient(circle at 45% 40%, var(--pattern-red) 0, transparent 30%),
      radial-gradient(circle at 80% 25%, var(--pattern-blue) 0, transparent 28%),
      radial-gradient(circle at 15% 80%, var(--pattern-orange) 0, transparent 28%),
      radial-gradient(circle at 48% 85%, var(--pattern-purple) 0, transparent 28%),
      radial-gradient(circle at 85% 78%, var(--pattern-orange) 0, transparent 30%),
      var(--card-bg);
  }
</style>
</head>
<body>
<main class="sheet">
  <section class="card card--front">
    <div class="identity">
      <div class="wordmark"><span class="wordmark__dot"></span>Kidvale</div>
      <div class="person__name">Liam Verster</div>
      <div class="person__title">Managing Director</div>
    </div>
    <div class="contact">
      <div class="contact__line">
        <svg class="contact__icon" viewBox="0 0 16 16" aria-hidden="true"><path d="M4 1.5l2.5 3-1.5 1.8c.8 1.8 2 3 3.8 3.8l1.8-1.5 3 2.5-1.6 2.4C7 13.3 2.7 9 1.5 3.1z" fill="none" stroke="var(--brand-blue)" stroke-width="1.5" stroke-linejoin="round"/></svg>
        <span>021 563 417</span>
      </div>
      <div class="contact__line">
        <svg class="contact__icon" viewBox="0 0 16 16" aria-hidden="true"><rect x="1.5" y="3.5" width="13" height="9" fill="none" stroke="var(--brand-blue)" stroke-width="1.4"/><path d="M1.5 3.5L8 9l6.5-5.5" fill="none" stroke="var(--brand-blue)" stroke-width="1.4"/></svg>
        <span>liam@kidvale.co.nz</span>
      </div>
      <div class="contact__line">
        <svg class="contact__icon" viewBox="0 0 16 16" aria-hidden="true"><circle cx="8" cy="8" r="6.3" fill="none" stroke="var(--brand-blue)" stroke-width="1.4"/><ellipse cx="8" cy="8" rx="2.8" ry="6.3" fill="none" stroke="var(--brand-blue)" stroke-width="1.2"/><path d="M1.7 8h12.6" stroke="var(--brand-blue)" stroke-width="1.2"/></svg>
        <span>www.kidvale.co.nz</span>
      </div>
      <div class="contact__address">
        <div>PO Box 318625</div>
        <div>Fernlea, Auckland</div>
      </div>
    </div>
  </section>

  <section class="card card--back">
    <div class="pattern" role="img" aria-label="Playful all-over pattern of colourful hand-drawn children, hearts, stars and swirls on white"></div>
  </section>
</main>
</body>
</html>
```